依頼詳細
WEB販売で高濃度アルコールのウェットシートを販売したいと考えております。
一般のお客様がこのチラシを見て購買意欲が出るような内容をお願い致します。
記載項目
①画像
・表面の商品画像(添付あり)

②文字
・裏面の注意事項(添付あり)
・アルコール75%
・除菌99.9%
・厚手シート
・除菌性能試験取得済
・拭くだけ簡単除菌!気になる菌・汚れに

③イラスト
・女性がテーブルやドアノブなどを拭いているイラスト
サイズ
A5
ページ数
両面
希望イメージ
シンプル 複雑
単色 カラフル
暗い 明るい
日常 高級
遊び心 厳粛
未来的 伝統的
女性的 男性的
希望する色
黄・オレンジ系、緑系、水色系
納品ファイル
• 高解像度JPG (.jpg)
• イラストレーター形式 (.ai)
補足説明
WEBで売られているウェットシートの広告のようなイメージです。
向きは縦でお願い致します。
■ 選んだ理由

分かりやすいデザインと使い方のピクトグラムが良かったので今回選ばせていただきました。

■ 提案者全員のお礼・コメント

皆様今回は弊社のデザインコンペにご参加くださり誠にありがとうございます。
どのデザインも素晴らしかったので決定するのが非常に難しかったです。

今後も不定期で依頼させていただきますのでご都合が合うようであれば是非ご参加ください。
引き続き宜しくお願い致します。

```html
<!DOCTYPE html>
<html lang="ja">
<head>
<meta charset="utf-8">
<title>除菌ウェットシート</title>
<link rel="stylesheet" href="https://fonts.googleapis.com/css2?family=Noto+Sans+JP:wght@500;700;900&display=swap">
<style>
  :root {
    --green: #2fa84a;
    --green-dark: #1f8a38;
    --yellow: #ffe100;
    --white: #ffffff;
    --bg: #f4faf3;
    --pack-light: #eef6ee;
    --pack-mid: #cfe8d1;
    --text: #2b2b2b;
  }
  * { margin: 0; padding: 0; box-sizing: border-box; }
  html, body { width: 847px; height: 1200px; overflow: hidden; }
  body { font-family: "Noto Sans JP", sans-serif; background: var(--bg); }
  .flyer { position: relative; width: 847px; height: 1200px; overflow: hidden; background: var(--bg); }

  .header { position: absolute; left: 0; top: 0; width: 847px; height: 240px; z-index: 2; }
  .header svg { position: absolute; inset: 0; }
  .title-main {
    position: absolute; left: 70px; top: 8px;
    font-size: 128px; font-weight: 900; color: var(--white); letter-spacing: 4px; line-height: 1.1;
  }
  .title-sub {
    position: absolute; left: 72px; top: 160px;
    background: var(--white); color: var(--green);
    font-size: 32px; font-weight: 900; padding: 2px 18px; border-radius: 6px;
  }
  .rate {
    position: absolute; left: 340px; top: -12px; white-space: nowrap;
    font-size: 176px; font-weight: 900; color: var(--yellow); line-height: 1.1; letter-spacing: -8px;
    -webkit-text-stroke: 4px var(--white); paint-order: stroke fill;
  }
  .rate .percent { font-size: 92px; letter-spacing: 0; margin-left: 6px; }
  .rate-note {
    position: absolute; left: 716px; top: 168px;
    display: flex; align-items: center; gap: 6px; color: var(--white); font-weight: 900;
  }
  .rate-note .small { font-size: 14px; line-height: 1.15; width: 34px; }
  .rate-note .big { font-size: 36px; line-height: 1; }

  .catch {
    position: absolute; left: 22px; top: 258px; height: 900px;
    writing-mode: vertical-rl; white-space: nowrap;
    font-size: 96px; font-weight: 900; color: var(--green);
    letter-spacing: 2px; line-height: 1;
  }

  .product {
    position: absolute; left: 150px; top: 250px; width: 500px; height: 870px;
    border-radius: 30px;
    background: linear-gradient(160deg, var(--pack-light) 0%, var(--white) 45%, var(--pack-mid) 100%);
    box-shadow: 0 10px 24px rgba(0,0,0,0.15);
    transform: rotate(-1.5deg);
  }

  .features { position: absolute; left: 680px; top: 225px; display: flex; flex-direction: column; gap: 50px; list-style: none; }
  .feature {
    width: 152px; height: 152px; border-radius: 50%; background: var(--green);
    display: flex; flex-direction: column; align-items: center; justify-content: center;
    color: var(--white); font-weight: 900; text-align: center; line-height: 1.15;
  }
  .feature .label { font-size: 24px; }
  .feature .value { font-size: 48px; line-height: 1; }
  .feature .big { font-size: 34px; }

  .footnote {
    position: absolute; left: 0; right: 0; top: 1150px; text-align: center;
    font-size: 14px; font-weight: 500; color: var(--text);
  }
</style>
</head>
<body>
<main class="flyer">
  <header class="header">
    <svg width="847" height="240" viewBox="0 0 847 240" aria-hidden="true">
      <polygon points="0,0 847,0 847,215 0,240" fill="var(--green)"/>
    </svg>
    <h1 class="title-main">除菌</h1>
    <div class="title-sub">ウェットシート</div>
    <div class="rate">99.9<span class="percent">%</span></div>
    <div class="rate-note"><span class="small">ウィルス<br>汚れ</span><span class="big">除去</span></div>
  </header>

  <p class="catch">拭くだけ簡単除菌!</p>

  <div class="product" role="img" aria-label="除菌ウェットシート 10枚入り 商品パッケージ(アルコール75%・厚手シート)"></div>

  <ul class="features">
    <li class="feature"><span class="label">アルコール</span><span class="value">75%</span></li>
    <li class="feature"><span class="big">厚手<br>シート</span></li>
    <li class="feature"><span class="big">菌・<br>汚れに</span></li>
  </ul>

  <p class="footnote">※除菌は全ての菌を除去するものではありません。</p>
</main>
</body>
</html>
```